Stationary design for construction company

Want professional stationary and in the future brochures to use for contacting potential customers and existing customers. We are open to suggestions with existing logo. We are a contractor in the construction field that specializes in foundation plastering. We currently do other work but are looking to market and become the only go-to subcontractor for this specialty. I like the red and black contrast and the font which is "biner d". We want to present ourselves as a professional company so potential customers take us seriously.
Dunmore Stucco
86 N. Maple #415
Ashgrove, Nevada 84093
801.574.2281 Office
801.846.5037 Mobile
marla@dunmorestucco-example.com
neil@dunmorestucco-example.com
We will need to be able to edit the finished work incase future numbers, addresses and such change.
Thx
Marla
Target Market(s)
New and exiting customers in the building industry
Industry/Entity Type
Construction Company
Font styles to use
Other font styles liked:
- Biner D
Look and feel
Each slider illustrates characteristics of the customer's brand and the style your logo design should communicate.

```html
<!DOCTYPE html>
<html lang="en">
<head>
<meta charset="utf-8">
<title>Dunmore Stucco – Business Card</title>
<link href="https://fonts.googleapis.com/css2?family=Source+Sans+3:wght@400;600;700&display=swap" rel="stylesheet">
<style>
  :root {
    --stage: #9c9c9c;
    --card-light: #e9e9eb;
    --card-dark: #000000;
    --brand-red: #a50f14;
    --ink: #1a1a1a;
    --ink-soft: #4a4a4a;
    --rule: #7a7a7a;
    --panel-tint: rgba(190, 150, 155, 0.18);
    --white: #ffffff;
  }
  * { box-sizing: border-box; margin: 0; padding: 0; }
  html, body {
    width: 1105px; height: 1200px; overflow: hidden;
    background: var(--stage);
    font-family: "Source Sans 3", "Myriad Pro", sans-serif;
  }
  .card {
    position: absolute; left: 180px;
    width: 746px; height: 426px; overflow: hidden;
  }
  .card--front { top: 120px; background: var(--card-light); }
  .card--back { top: 637px; background: var(--card-dark); }

  .panel { position: absolute; background: var(--panel-tint); }
  .panel--tall { left: 12px; top: 7px; width: 134px; height: 287px; }
  .panel--mid { left: 159px; top: 7px; width: 148px; height: 280px; }
  .panel--low { left: 159px; top: 294px; width: 148px; height: 110px; }

  .wordmark { position: absolute; display: flex; align-items: center; gap: 8px; }
  .wordmark__square { background: var(--brand-red); flex: none; }
  .wordmark__name {
    font-weight: 700; text-transform: uppercase; line-height: 0.98; letter-spacing: 1px;
  }
  .card--front .wordmark { left: 405px; top: 55px; }
  .card--front .wordmark__square { width: 65px; height: 94px; }
  .card--front .wordmark__name { font-size: 46px; color: var(--ink); }

  .card--back .wordmark { left: 207px; top: 181px; gap: 10px; }
  .card--back .wordmark__square { width: 69px; height: 105px; }
  .card--back .wordmark__name { font-size: 51px; color: var(--white); }

  .company-name {
    position: absolute; left: 40px; top: 218px;
    font-size: 27px; font-weight: 600; color: var(--brand-red);
  }
  .divider {
    position: absolute; left: 40px; top: 257px; width: 662px; height: 1px;
    background: var(--rule);
  }
  .contact-list { position: absolute; left: 44px; top: 272px; list-style: none; }
  .contact-list li {
    display: flex; align-items: center; gap: 9px;
    height: 28.7px; font-size: 19.5px; color: var(--ink-soft);
  }
  .contact-list svg { width: 16px; height: 16px; fill: var(--brand-red); flex: none; }
  .address {
    position: absolute; right: 44px; top: 295px; text-align: right;
    font-style: normal; font-size: 19.5px; line-height: 28.7px; color: var(--ink-soft);
  }
  .edge-band { position: absolute; left: 0; bottom: 0; width: 746px; height: 17px; }
</style>
</head>
<body>
  <section class="card card--front" aria-label="Business card front">
    <div class="panel panel--tall"></div>
    <div class="panel panel--mid"></div>
    <div class="panel panel--low"></div>

    <div class="wordmark">
      <span class="wordmark__square"></span>
      <span class="wordmark__name">Dunmore<br>Stucco</span>
    </div>

    <h1 class="company-name">Dunmore Stucco</h1>
    <div class="divider"></div>

    <ul class="contact-list">
      <li><svg viewBox="0 0 16 16" aria-hidden="true"><path d="M3.2 1.2l2.4 0 1.2 3.2-1.6 1.2a8 8 0 0 0 5.2 5.2l1.2-1.6 3.2 1.2v2.4c0 .9-.8 1.6-1.7 1.6C6.8 14.4 1.6 9.2 1.6 2.9c0-.9.7-1.7 1.6-1.7z"/></svg>801.574.2281</li>
      <li><svg viewBox="0 0 16 16" aria-hidden="true"><path d="M4.5 0.5h7a1 1 0 0 1 1 1v13a1 1 0 0 1-1 1h-7a1 1 0 0 1-1-1v-13a1 1 0 0 1 1-1zm1 2v9.5h5V2.5zm2.5 10.5a.9.9 0 1 0 0 1.8.9.9 0 0 0 0-1.8z"/></svg>801.846.5037</li>
      <li><svg viewBox="0 0 16 16" aria-hidden="true"><path d="M1 3.5h14v9H1zm1.3 1.2L8 9l5.7-4.3z"/></svg>marla@dunmorestucco-example.com</li>
      <li><svg viewBox="0 0 16 16" aria-hidden="true"><path d="M1 3.5h14v9H1zm1.3 1.2L8 9l5.7-4.3z"/></svg>neil@dunmorestucco-example.com</li>
    </ul>

    <address class="address">
      86 N. Maple #415<br>
      Ashgrove, Nevada 84093<br>
      www.dunmorestucco-example.com
    </address>

    <svg class="edge-band" viewBox="0 0 746 17" preserveAspectRatio="none" aria-hidden="true">
      <polygon points="0,0 491,0 486,17 0,17" fill="var(--brand-red)"/>
      <polygon points="496,0 746,0 746,17 491,17" fill="var(--card-dark)"/>
    </svg>
  </section>

  <section class="card card--back" aria-label="Business card back">
    <div class="wordmark">
      <span class="wordmark__square"></span>
      <span class="wordmark__name">Dunmore<br>Stucco</span>
    </div>
  </section>
</body>
</html>
```